Lantern Co. Supplement General Packaging Design

I am looking for a design template to design all of my various supplements and other products around. Meaning that this design should be able to just be able to change around words, up to a few small images, and text to suit my other various products.

The brand name is Lantern Co. and the slogan is: Heros Are Made
This is For an Apple Cider Vinegar Gummy, and include these top three things: Vegan, Gluten Free, Non-GMO somewhere in the design.

I want the design to have a luxurious feel. With some kind of design element where the logo is sort of the secondary aspect of the design.

Target Market(s)

Men age 24-45

Industry/Entity Type

Supplement

Requirements
Must have
• MUST HAVE A "vintage" LOOK AND FEEL. MUST HAVE ANOTHER design element besides the logo. (Something Vintage) MUST USE THE PROVIDED TEMPLATE A PDF IN THE FILES BELOW LABELED " TEMPLATE" and the LOGO PROVIDED under "Lantern Co. 2" OR "Lantern Co.3" whichever is better suited for the design. Bold design. Another color besides black to stand out. Use the lantern co logo which is below in the provided images. The design should go around the logo and fit the same aesthetic. The rest are for inspiration, what I like.

```html
<!DOCTYPE html>
<html lang="en">
<head>
<meta charset="utf-8">
<title>Lantern Co. – Supplement Label</title>
<link rel="stylesheet" href="https://fonts.googleapis.com/css2?family=Jost:wght@200;400;500&display=swap">
<style>
  :root {
    --bg: #141414;
    --gold: #e3bf52;
    --gold-light: #f7e08a;
    --gold-deep: #b8861f;
  }
  html, body {
    margin: 0;
    padding: 0;
    overflow: hidden;
    background: var(--bg);
  }
  .label {
    position: relative;
    width: 1200px;
    height: 1200px;
    background: var(--bg);
    overflow: hidden;
    font-family: "Jost", sans-serif;
    color: var(--gold);
  }
  .frame {
    position: absolute;
    inset: 0;
  }
  .brand-mark {
    position: absolute;
    left: 495px;
    top: 352px;
    width: 210px;
    height: 210px;
    border-radius: 50%;
    background: radial-gradient(circle at 40% 35%, var(--gold-light), var(--gold) 45%, var(--gold-deep));
  }
  .brand-name {
    position: absolute;
    left: 0;
    width: 1200px;
    top: 632px;
    margin: 0;
    text-align: center;
    font-weight: 200;
    font-size: 68px;
    letter-spacing: 3px;
    line-height: 1;
    text-transform: uppercase;
    color: var(--gold);
  }
  .slogan-row {
    position: absolute;
    left: 177px;
    width: 840px;
    top: 764px;
    height: 36px;
    display: flex;
    align-items: center;
    gap: 36px;
  }
  .slogan-rule {
    flex: 1;
    height: 2px;
    background: linear-gradient(90deg, var(--gold-deep), var(--gold-light), var(--gold-deep));
  }
  .slogan {
    margin: 0;
    font-weight: 400;
    font-size: 27px;
    letter-spacing: 0.5px;
    text-transform: uppercase;
    color: var(--gold);
    white-space: nowrap;
  }
  .claims {
    position: absolute;
    left: 0;
    width: 1200px;
    top: 856px;
    margin: 0;
    text-align: center;
    font-weight: 500;
    font-size: 17px;
    letter-spacing: 0.3px;
    text-transform: uppercase;
    color: var(--gold);
    white-space: pre;
  }
</style>
</head>
<body>
<main class="label">
  <svg class="frame" width="1200" height="1200" viewBox="0 0 1200 1200" aria-hidden="true">
    <defs>
      <linearGradient id="goldStroke" x1="0" y1="0" x2="1" y2="1">
        <stop offset="0" stop-color="#b8861f"/>
        <stop offset="0.3" stop-color="#f7e08a"/>
        <stop offset="0.55" stop-color="#c99a2e"/>
        <stop offset="0.8" stop-color="#f2d677"/>
        <stop offset="1" stop-color="#b8861f"/>
      </linearGradient>
    </defs>
    <path class="frame-outer" fill="none" stroke="url(#goldStroke)" stroke-width="4"
      d="M210 112 H990 A98 98 0 0 0 1088 210 V990 A98 98 0 0 0 990 1088 H210 A98 98 0 0 0 112 990 V210 A98 98 0 0 0 210 112 Z"/>
    <path class="frame-inner" fill="none" stroke="url(#goldStroke)" stroke-width="3"
      d="M227 134 H973 A117 117 0 0 0 1066 227 V973 A117 117 0 0 0 973 1066 H227 A117 117 0 0 0 134 973 V227 A117 117 0 0 0 227 134 Z"/>
  </svg>

  <div class="brand-mark" role="img" aria-label="Lantern Co. brand mark"></div>

  <h1 class="brand-name">Lantern Co.</h1>

  <div class="slogan-row">
    <span class="slogan-rule"></span>
    <p class="slogan">Heros Are Made</p>
    <span class="slogan-rule"></span>
  </div>

  <p class="claims">Vegan, Gluten Free  &amp; Non-GMO Supplement</p>
</main>
</body>
</html>
```